Website for the recruitment firm velmo

Objective :

Create a modern, elegant, and understated website with a touch of sophistication. The site must be fully custom-coded (or custom-coded on WordPress), responsive, and fast, reflecting the quality and high standards of our firm.

It must be bilingual (FR/EN), with a language selector visible in the header.

About velmo.

velmo. is a high-end recruitment firm, led by experienced consultants—employees and freelancers—and supported by a dedicated team of recruitment managers. Our hybrid approach allows us to handle complex, confidential, or high-volume projects with rigor and agility.

We operate across several business verticals:

Executive

Finance & Advisory (accounting, management control, treasury, corporate finance, financial consulting or investment banking)

Legal

Audit & Expertise

People & Office

Supply & Purchasing

Industry & Engineering

Our approach is based on a balance between human know-how and cutting-edge technologies (AI, automation, data) to respond to recruitment challenges with accuracy, responsiveness and impact.

Slogan: Expertise at the service of every recruitment.

Purpose of the site:

Client side: present our expertise, our values, our support.

Candidate side: allow the search for offers, by expertise.

On the consultant side: encouraging freelancers or employees to join us.

Structure & pages requested:

Welcome

Main banner with slogan and strong visual (possibility of a background video like maisontalvo.example — for a modern and dynamic look)

Clear redirection to both paths: “I’m looking for talent” / “I want to join velmo. ”

Quick presentation of expertise with redirection to each dedicated page

Highlighting values

About

Our mission

Our values (excellence, flexibility, partnership)

Our hybrid operation (in-house and independent consultants)

The recruitment team and the support offered

Expertise (1 page per vertical, with color code specific to each division)

Description of the professions recruited

Key skills

Typical customer profiles

Testimonials or case studies (placeholder)

Button/CTA to offers corresponding to this expertise

Job offers

Page with filter by expertise

“Join velmo” option with our internal offers (consultants, recruitment managers, etc.)

Join us

Why work with velmo.

Independent vs. employee path

Tools provided, support, internal training

Highlighting the support team and recruitment managers

Contact

Form

Email + LinkedIn link

Design requirements:

Font: Gazette LT Std or contemporary serif with a strong identity

Color code by division (the background or page elements must match the color of the expertise):

velmo. / velmo.group. → #000000 (black)

velmo.executive. → #2F4F4F (dark green)

velmo.finance&advisory. → #0B1E36 (midnight blue)

velmo.people&office. → #f2b8b8 (powder pink)

velmo.audit&expertise. → #993294 (plum)

velmo.legal. → #d9a00f (yellow gold)

velmo.supply&purchasing. → #CE8946 (rust bronze)

velmo.industry&engineering. → #9e9b9e (light silver gray)

Technical features:

100% responsive and mobile-friendly design

Fast charging

Own structure (SEO-friendly)

Simple back-office interface for updating offers

Language selector FR / EN

Inspirations to consult:

For the tree structure, tabs and ergonomics: bristow-lane.example

For visual ambiance / video / animation: maisontalvo.example

Expected deliverables:

Full site (online or compressed file)

All source files (HTML/CSS/JS or custom Wordpress)

Favicon

Brand guideline (PDF) with:

Typographies used

HEX color codes

Margins and line spacing

Examples of use of light and dark background logo

Optional: template for email signature

Objective
Design a modern, elegant and clean website with a touch of sophistication. The site must be fully custom-coded (or built with custom WordPress development), responsive, fast, and reflect the premium standards and quality of our recruitment firm.

It must be bilingual (FR/EN), with a clearly visible language selector in the header.

About velmo.
velmo. is a premium recruitment firm driven by experienced consultants — whether in-house or freelance — supported by a dedicated team of recruitment coordinators. Our hybrid model allows us to handle complex, confidential, or high-volume recruitment assignments with both precision and agility.

We operate across several verticals:

Executive

Finance & Advisory (accounting, controlling, treasury, corporate finance, investment banking advisory)

Legal

Audit & Expertise

People & Office

Supply & Purchasing

Industry & Engineering

Our approach combines human expertise with cutting-edge technologies (AI, automation, data) to tackle recruitment challenges with accuracy, speed, and impact.

Tagline: Expertise serving every recruitment need.

Website Purpose
Client-facing: highlight our expertise, values, and recruitment support model.

Candidate-facing: allow job seekers to explore openings by area of expertise.

Consultant-facing: attract freelance or in-house recruiters to join velmo.

Site Structure & Required Pages
Home
Hero banner with tagline and impactful visual (option for background video, eg maisontalvo. That)

Clear user path: “I'm looking to hire” / “I want to join velmo. ”

Quick intro to our expertise areas with links to each division page

Highlight our values and unique model

About Us
Our mission

Our hybrid recruitment model (internal consultants + freelancers)

Our recruitment support team and how we work

Expertise (1 page per vertical, using the division's brand color)
Each division page should include:

Description of roles we recruit

Key skills

Typical client profiles

Placeholder for testimonials or success stories

CTA linking to job openings relevant to the division

Verticals:

Executive

Finance & Advisory

Legal

Audit & Expertise

People & Office

Supply & Purchasing

Industry & Engineering

Job Offers
Central job board with filter by expertise

Section: “Join velmo. ” with internal positions (consultants, recruitment coordinators, etc.)

Join Us
Why join velmo.

Independent vs. permanent contract path

Tools, training and operational support

Highlight the internal sourcing and recruitment support team

Contact
Contact form

Email + LinkedIn link

Design Requirements
Font: Gazette LT Std or similar contemporary serif with strong identity

Each vertical should have its own dedicated brand color applied to its page background or key elements:

Division HEX Code Color Description
velmo. /velmo.group. #000000 Black
velmo.executive #2F4F4F Dark green
velmo.finance&advisory #0B1E36 Navy blue
velmo.people&office #f2b8b8 Powder pink
velmo.audit&expertise #993294 Plum
velmo.legal #d9a00f Golden yellow
velmo.supply&purchasing #CE8946 Rust bronze
velmo. industry&engineering #9e9b9e Light silver gray

Technical Features
Fully responsive and mobile-friendly

Fast loading

Clean structure, SEO optimized

Simple back-office interface for job posting and updates

Bilingual switch: FR / EN

Inspirations
For navigation, structure, and user interface:
🔗 https://www.bristow-lane.example/fr/fr/

For visual style, animations, and dynamic video intro:
🔗 https://maisontalvo.example/

Deliverables
Fully functional website (live or delivered as a complete package)

All source files (HTML/CSS/JS or custom WordPress)

Favicon

Brand guideline (PDF) including:

Fonts used

HEX color codes

Spacing and layout guidelines

Logo usage on dark/light backgrounds

Optional: email signature template

Hi, A few clarifications to guide the website structure. The site should be clearly built around three main sections, each addressing a specific target audience: 1. For Clients – “Looking to hire?” This section will highlight our recruitment services, industry expertise, and tailored approach. 2. For Candidates – “Looking for a job?” A space where candidates can explore job offers by sector and apply directly. 3. For Experts – “Want to join us?” This area is for recruitment professionals (consultants or talent acquisition specialists) interested in joining velmo., either as employees or as independents. It should showcase the tools, support, and working environment we offer. These three user paths should be clearly visible on the homepage, using clear buttons or dedicated sections to ensure smooth navigation.

• Gazette LT Std

• Essentials – Section Ideas Our hybrid model → Clear presentation of employee/freelance cohabitation, and how it brings flexibility and efficiency to clients. Our quality commitment → Rigorous methodology, transparency, customer satisfaction, tailor-made support. Our augmented approach → Highlighting the use of AI tools, intelligent CRM, automated multi-channel sourcing, predictive tests, etc. Our support team → Promotion of the team of recruitment managers who support the consultants, guaranteeing responsiveness and depth in the hunt. Our areas of expertise → Mini-grid or mosaic that links to the main verticals (useful for cross-functional reinforcement).
• CRM / ATS Integration Direct connection with our application management tool (Dorveta type or other), for seamless synchronization of offers, applications and follow-ups. 📱 Progressive web app version (PWA) A site accessible in mobile application mode, for a smooth, fast and accessible offline user experience.

```html
<!DOCTYPE html>
<html lang="en">
<head>
<meta charset="utf-8">
<title>velmo. — finance &amp; advisory recruitment</title>
<link href="https://fonts.googleapis.com/css2?family=Prata&family=Inter:wght@400;500;600&family=Poppins:wght@400;500;600&display=swap" rel="stylesheet">
<style>
:root{
  --navy:#0b1e36;
  --ink:#14161a;
  --muted:#6b7280;
  --paper:#ffffff;
  --div-executive:#2f4f4f;
  --div-finance:#0b1e36;
  --div-legal:#d9a00f;
  --div-audit:#993294;
  --div-people:#f2b8b8;
  --div-supply:#ce8946;
  --div-industry:#9e9b9e;
  --serif:'Prata', Georgia, serif;
  --sans:'Inter', Arial, sans-serif;
  --round:'Poppins', Arial, sans-serif;
}
*{box-sizing:border-box;margin:0;padding:0}
html,body{width:1200px;height:3807px;overflow:hidden;background:var(--paper);color:var(--ink);font-family:var(--sans)}
.page{position:relative;width:1200px;height:3807px;overflow:hidden}
.abs{position:absolute}
.serif{font-family:var(--serif);font-weight:400}

/* header */
.brand{left:60px;top:14px;width:110px;height:48px;background:var(--navy);border-radius:6px;color:#fff;font-family:var(--serif);font-size:24px;display:flex;align-items:center;justify-content:center}
.nav{left:384px;top:28px;display:flex;gap:30px;font-size:15px;color:#7a8190}
.nav .active{color:var(--ink);font-weight:600;text-decoration:underline}
.lang{left:918px;top:26px;display:flex;align-items:center;gap:6px;font-size:13px;font-weight:600;color:#7a8190}
.lang .on{color:var(--navy)}
.lang i{width:1px;height:14px;background:#9aa2ae}
.btn-contact{left:1012px;top:16px;width:130px;height:44px;background:var(--navy);color:#fff;border-radius:5px;font-size:15px;font-weight:500;display:flex;align-items:center;justify-content:center}

/* hero */
.hero-visual{left:0;top:0;width:1200px;height:710px;background:linear-gradient(90deg,#e9edf2 0%,#cfd6df 30%,#b9c2cd 50%,#dfe3e9 70%,#f4f5f7 100%)}
.hero-fade{left:0;top:0;width:620px;height:710px;background:linear-gradient(90deg,rgba(240,242,246,.95),rgba(240,242,246,.6) 70%,rgba(240,242,246,0))}
.tag{left:60px;top:197px;width:144px;height:24px;background:var(--navy);color:#fff;font-size:10px;letter-spacing:4px;border-radius:3px;display:flex;align-items:center;justify-content:center}
.h1{left:60px;top:232px;font-size:54px;line-height:1.1;color:var(--navy)}
.h1b{left:60px;top:299px;font-size:34px;color:var(--navy)}
.hero-p{left:60px;top:362px;width:470px;font-size:15px;line-height:27px;color:#2a2f38}
.path{top:439px;width:214px;height:74px;background:var(--navy);color:#fff;border-radius:6px;padding:12px 9px}
.path b{display:block;font-family:var(--serif);font-weight:400;font-size:11.5px;white-space:nowrap;margin-bottom:9px}
.path span{display:block;font-size:8.5px;line-height:15px;color:#cdd4de}
.play{left:961px;top:313px}

/* about */
.h2{font-size:42px;color:var(--navy);letter-spacing:.5px}
.about-h{left:60px;top:808px}
.about-sub{left:60px;top:884px;font-size:28px;line-height:40px;color:var(--ink);width:420px}
.about-p{left:60px;top:977px;width:400px;font-size:14px;line-height:26px;color:var(--muted)}
.stat{top:1082px;font-family:var(--serif);font-size:44px;color:var(--navy)}
.stat-l{top:1153px;font-size:18px;line-height:21px;color:var(--ink)}
.btn-sm{left:60px;top:1240px;width:127px;height:35px;background:var(--navy);color:#fff;border-radius:4px;font-family:var(--serif);font-size:14px;display:flex;align-items:center;justify-content:center}
.about-photo{left:494px;top:823px;width:350px;height:452px;border-radius:10px;background:linear-gradient(160deg,#c9ccd1,#8c96a3 55%,#2d3a4f)}
.mission{left:881px;top:823px;width:260px;height:262px;background:var(--navy);border-radius:6px;color:#fff;padding:24px 12px}
.mission h3{font-size:18px;font-weight:600;margin-bottom:16px}
.mission p{font-size:10px;line-height:19.5px;color:#cfd6e0}
.arrow{position:absolute;right:14px;top:24px}
.pill{left:881px;width:260px;height:77px;border:2px solid #e6e9ee;border-radius:6px;box-shadow:0 2px 6px rgba(0,0,0,.08);display:flex;align-items:center;padding:0 12px;font-size:18px}
.pill svg{position:absolute;right:26px}

/* expertise */
.exp-band{left:0;top:1389px;width:1200px;height:721px;background:linear-gradient(180deg,#e6eaef,#f1f3f6 40%,#e9ecf0)}
.center{left:0;width:1200px;text-align:center}
.exp-sub{top:1493px;font-size:28px;color:var(--ink)}
.card-img{top:1584px;width:255px;height:300px;border-radius:6px}
.card-lbl{top:1899px;width:255px;height:80px;background:var(--navy);border-radius:5px;color:#fff;padding:8px 10px;border-top:4px solid var(--div)}
.card-lbl b{display:block;font-family:var(--serif);font-weight:400;font-size:18px;margin-bottom:2px}
.card-lbl span{display:block;font-size:11px;line-height:18px;color:#d3d9e2}
.slider-track{left:170px;top:2044px;width:880px;height:3px;background:var(--navy)}
.count{left:1066px;top:2026px;font-family:var(--round);font-size:28px;font-weight:600;color:var(--navy)}
.count small{font-size:17px}

/* jobs */
.jobs-sub{top:2284px;font-size:28px}
.job{top:2415px;width:258px;height:165px;border:2px solid #e3e6eb;border-radius:10px;padding:5px;box-shadow:0 2px 6px rgba(0,0,0,.06)}
.job-in{width:100%;height:100%;border:3px solid var(--navy);border-radius:8px;text-align:center;padding-top:58px}
.job-in h4{font-family:var(--round);font-weight:600;font-size:19px;color:var(--ink);margin-bottom:8px}
.job-in p{font-size:12px;line-height:19px;color:#3b414b}
.job.dark .job-in{background:var(--navy)}
.job.dark h4,.job.dark p{color:#fff}
.job-icon{top:2378px;width:80px;height:80px;border-radius:50%;background:#fff;border:3px solid var(--navy);display:flex;align-items:center;justify-content:center}
.job-icon.dark{background:var(--navy);border-color:#fff;box-shadow:0 0 0 2px var(--navy)}

/* contact */
.contact-sub{top:2756px;font-size:28px}
.ci{top:2850px;width:52px;height:52px;background:var(--navy);border-radius:12px;display:flex;align-items:center;justify-content:center}
.ci-t{top:2911px;width:220px;text-align:center;font-family:var(--round);font-size:12px;line-height:19px;color:#2b2f36}
.field{height:57px;border:2px solid #e6e8ec;border-radius:10px;padding:0 22px;display:flex;align-items:center;font-size:15px;color:#6b7280}
.area{align-items:flex-start;padding-top:22px}
.submit{left:136px;top:3268px;width:928px;height:38px;background:var(--navy);border-radius:4px;color:#fff;font-size:15px;font-weight:600;display:flex;align-items:center;justify-content:center}

/* footer */
.footer{left:0;top:3420px;width:1200px;height:387px;background:var(--navy)}
.footer-map{left:540px;top:3420px;width:660px;height:320px;background:radial-gradient(ellipse at 50% 50%,rgba(60,86,124,.35),rgba(11,30,54,0) 70%)}
.f-brand{left:60px;top:3492px;font-family:var(--serif);font-size:64px;color:#fff;line-height:1}
.f-brand small{display:block;font-size:16px;margin-top:2px}
.f-p{left:60px;top:3590px;width:360px;font-size:15px;line-height:24px;color:#e4e9f0}
.soc{top:3662px;width:30px;height:30px;border-radius:50%;background:#fff}
.f-h{top:3508px;font-family:var(--serif);font-size:19px;color:#fff}
.f-l{top:3558px;font-size:12px;line-height:28px;color:#d8dfe8}
.f-rule{left:60px;top:3748px;width:1080px;height:1px;background:#8a98ad}
.f-b{top:3768px;font-size:11px;color:#c9d1dc}
</style>
</head>
<body>
<main class="page">

  <section>
    <div class="abs hero-visual" role="img" aria-label="Two consultants in suits reviewing documents at a desk, with a city skyline behind"></div>
    <div class="abs hero-fade"></div>
    <div class="abs brand">velmo.</div>
    <nav class="abs nav"><span class="active">Home</span><span>About Us</span><span>Areas Of Expertise</span><span>Job Offers</span></nav>
    <div class="abs lang" aria-label="Language"><span>FR</span><i></i><span class="on">EN</span></div>
    <div class="abs btn-contact">Contact Us</div>

    <div class="abs tag">CONSULTANTES</div>
    <h1 class="abs h1 serif">EXPERTISE.</h1>
    <div class="abs h1b serif">PRÉCISION. RECRUTEMENT.</div>
    <p class="abs hero-p">At Havenly Accessible Modifications, We Specialize In Making Homes Safer And More Accessible</p>
    <div class="abs path" style="left:60px"><b>JE RECHERCHE DES TALENTS</b><span>At HavenlyAccessible Modifications Specialize In Making Homes Safer</span></div>
    <div class="abs path" style="left:286px"><b>JE VEUX REJOINDRE VELMO</b><span>At HavenlyAccessible Modifications Specialize In Making Homes Safer</span></div>
    <svg class="abs play" width="84" height="84" viewBox="0 0 84 84" aria-label="Play video">
      <circle cx="42" cy="42" r="42" fill="rgba(255,255,255,.75)"/>
      <path d="M33 27 L59 42 L33 57 Z" fill="#2b3240"/>
    </svg>
  </section>

  <section>
    <h2 class="abs h2 serif about-h">ABOUT US</h2>
    <div class="abs about-sub">Built On Excellence, Driven By People</div>
    <p class="abs about-p">Lorem Ipsum Dolor Sit Amet Consectetur. Velit Tortor Molestie Praesent Est Eget Etiam Consequat. Nibh Tristique Vel Ut.</p>
    <div class="abs stat" style="left:60px">20+</div>
    <div class="abs stat" style="left:247px">99%</div>
    <div class="abs stat-l" style="left:60px">years of<br>experience</div>
    <div class="abs stat-l" style="left:247px">customer<br>satisfaction</div>
    <div class="abs btn-sm">Learn MOre</div>

    <div class="abs about-photo" role="img" aria-label="Team of colleagues gathered around a laptop in a meeting"></div>

    <div class="abs mission">
      <h3>Our Mission</h3>
      <svg class="arrow" width="26" height="26" viewBox="0 0 26 26"><circle cx="13" cy="13" r="12" fill="none" stroke="#fff" stroke-width="2"/><path d="M9 17 L17 9 M11 9 H17 V15" stroke="#fff" stroke-width="2" fill="none"/></svg>
      <p>Lorem Ipsum Dolor Sit Amet Consectetur. Velit Tortor Molestie Praesent Est Eget Etiam Consequat. Nibh Tristique Vel Ut Hac Odio Ut Tempor TurpisLorem Ipsum Dolor Sit Amet Consectetur. Velit Tortor Molestie Praesent Est Eget Etiam Consequat. Nibh Tristique Vel Ut Hac Odio Ut Tempor Turpis Lorem Ipsum Dolor Sit Amet Consectetur. Velit Tortor Molestie Praesent Est Eget Etiam Consequat. Nibh Tristique</p>
    </div>
    <div class="abs pill" style="top:1105px">Our Vision
      <svg width="26" height="26" viewBox="0 0 26 26"><circle cx="13" cy="13" r="13" fill="var(--navy)"/><path d="M9 17 L17 9 M11 9 H17 V15" stroke="#fff" stroke-width="2" fill="none"/></svg></div>
    <div class="abs pill" style="top:1200px">Our Story
      <svg width="26" height="26" viewBox="0 0 26 26"><circle cx="13" cy="13" r="13" fill="var(--navy)"/><path d="M9 17 L17 9 M11 9 H17 V15" stroke="#fff" stroke-width="2" fill="none"/></svg></div>
  </section>

  <section>
    <div class="abs exp-band" role="img" aria-label="Softly faded office interior with tall windows"></div>
    <h2 class="abs h2 serif center" style="top:1420px">AREAS OF EXPERTISE</h2>
    <div class="abs center exp-sub">Specialized Recruitment Across Every Industry We Know Best</div>

    <div class="abs card-img" style="left:60px;background:linear-gradient(160deg,#b8c4c8,#3d5a5c 60%,#1f3b3e)" role="img" aria-label="Executive in a green shirt standing with arms crossed"></div>
    <div class="abs card-img" style="left:334px;background:linear-gradient(160deg,#8a6a4a,#c9b79f 50%,#5e6570)" role="img" aria-label="Advisor working on a laptop in a lounge"></div>
    <div class="abs card-img" style="left:609px;background:linear-gradient(160deg,#3a3f47,#6f7680 50%,#c7c9cc)" role="img" aria-label="Hands gesturing over a laptop during a legal discussion"></div>
    <div class="abs card-img" style="left:883px;background:linear-gradient(160deg,#e7e8ea,#bfc3c8 50%,#8d8a73)" role="img" aria-label="Magnifying glass over audit documents"></div>

    <div class="abs card-lbl" style="left:60px;--div:var(--div-executive)"><b>Executive</b><span>Lorem Ipsum Dolor Sit Amet Consectetur. Nibh Neque Cras Mattis.</span></div>
    <div class="abs card-lbl" style="left:334px;--div:#3c5a86"><b>Finance &amp; Advisory</b><span>Lorem Ipsum Dolor Sit Amet Consectetur. Nibh Neque Cras Mattis.</span></div>
    <div class="abs card-lbl" style="left:609px;--div:var(--div-legal)"><b>Legal</b><span>Lorem Ipsum Dolor Sit Amet Consectetur. Nibh Neque Cras Mattis.</span></div>
    <div class="abs card-lbl" style="left:883px;--div:var(--div-audit)"><b>Audit &amp; Expertise</b><span>Lorem Ipsum Dolor Sit Amet Consectetur. Nibh Neque Cras Mattis.</span></div>

    <svg class="abs" style="left:58px;top:2026px" width="100" height="40" viewBox="0 0 100 40" aria-label="Previous and next">
      <circle cx="20" cy="20" r="18" fill="none" stroke="var(--navy)" stroke-width="2"/>
      <path d="M23 12 L15 20 L23 28" fill="none" stroke="var(--navy)" stroke-width="2"/>
      <circle cx="76" cy="20" r="18" fill="none" stroke="var(--navy)" stroke-width="2"/>
      <path d="M73 12 L81 20 L73 28" fill="none" stroke="var(--navy)" stroke-width="2"/>
    </svg>
    <div class="abs slider-track"></div>
    <div class="abs count">01<small>/ 02</small></div>
  </section>

  <section>
    <h2 class="abs h2 serif center" style="top:2210px">JOB OFFERS</h2>
    <div class="abs center jobs-sub">Handpicked Positions For High-Performing Professional</div>

    <div class="abs job" style="left:60px"><div class="job-in"><h4>Executive</h4><p>We listen, we care, and we act.<br>Your voice shapes the care</p></div></div>
    <div class="abs job dark" style="left:334px"><div class="job-in"><h4>Finance &amp; Advisory</h4><p>We listen, we care, and we act.<br>Your voice shapes the care</p></div></div>
    <div class="abs job" style="left:608px"><div class="job-in"><h4>Legal</h4><p>We listen, we care, and we act.<br>Your voice shapes the care</p></div></div>
    <div class="abs job" style="left:882px"><div class="job-in"><h4>Audit &amp; Expertise</h4><p>We listen, we care, and we act.<br>Your voice shapes the care</p></div></div>

    <div class="abs job-icon" style="left:150px"><svg width="40" height="40" viewBox="0 0 40 40" fill="none" stroke="var(--navy)" stroke-width="1.8"><circle cx="14" cy="13" r="5"/><path d="M5 33 C5 24 23 24 23 33"/><rect x="24" y="8" width="12" height="10"/><path d="M26 15 L29 12 L32 14 L34 10"/></svg></div>
    <div class="abs job-icon dark" style="left:424px"><svg width="40" height="40" viewBox="0 0 40 40" fill="none" stroke="#fff" stroke-width="1.8"><circle cx="22" cy="11" r="7"/><path d="M22 7 V15"/><path d="M5 27 L13 24 L22 26 L30 22 C33 21 34 24 31 26 L20 32 L5 31"/></svg></div>
    <div class="abs job-icon" style="left:698px"><svg width="40" height="40" viewBox="0 0 40 40" fill="none" stroke="var(--navy)" stroke-width="1.8"><path d="M9 5 H24 L30 11 V35 H9 Z"/><path d="M13 14 H25 M13 19 H25 M13 24 H20"/><path d="M22 30 L32 20 L35 23 L25 33 Z"/></svg></div>
    <div class="abs job-icon" style="left:972px"><svg width="40" height="40" viewBox="0 0 40 40" fill="none" stroke="var(--navy)" stroke-width="1.8"><rect x="8" y="5" width="22" height="28"/><path d="M12 10 H26 M12 15 H26 M12 20 H20"/><circle cx="25" cy="26" r="6"/><path d="M29 30 L34 35"/></svg></div>
  </section>

  <section>
    <h2 class="abs h2 serif center" style="top:2680px">CONTACT US</h2>
    <div class="abs center contact-sub">Let’s Connect And Start The Conversatio</div>

    <div class="abs ci" style="left:232px"><svg width="26" height="26" viewBox="0 0 24 24" fill="#fff"><path d="M6.6 10.8a15 15 0 0 0 6.6 6.6l2.2-2.2a1 1 0 0 1 1-.25 11.4 11.4 0 0 0 3.6.57 1 1 0 0 1 1 1V20a1 1 0 0 1-1 1A17 17 0 0 1 3 4a1 1 0 0 1 1-1h3.5a1 1 0 0 1 1 1c0 1.25.2 2.45.57 3.57a1 1 0 0 1-.25 1z"/></svg></div>
    <div class="abs ci" style="left:550px"><svg width="26" height="26" viewBox="0 0 24 24" fill="#fff"><path d="M12 2a7 7 0 0 0-7 7c0 5.2 7 13 7 13s7-7.8 7-13a7 7 0 0 0-7-7zm0 9.5A2.5 2.5 0 1 1 12 6.5a2.5 2.5 0 0 1 0 5z"/></svg></div>
    <div class="abs ci" style="left:887px"><svg width="28" height="28" viewBox="0 0 24 24" fill="#fff"><path d="M3 6h18v12H3z"/><path d="M3 6l9 7 9-7" fill="none" stroke="var(--navy)" stroke-width="1.8"/></svg></div>

    <div class="abs ci-t" style="left:152px">(480) 555-0149<br>(252) 555-0172</div>
    <div class="abs ci-t" style="left:466px">48 Linden Row, Fairhaven,<br>Oregon 97321</div>
    <div class="abs ci-t" style="left:803px">Nora.Pelling@velmo<br>.example</div>

    <div class="abs field" style="left:136px;top:2972px;width:454px">Fiest Name</div>
    <div class="abs field" style="left:610px;top:2972px;width:454px">Last Name</div>
    <div class="abs field" style="left:136px;top:3043px;width:454px">Phone Number</div>
    <div class="abs field" style="left:610px;top:3043px;width:454px">Email</div>
    <div class="abs field area" style="left:136px;top:3114px;width:928px;height:133px">Messages</div>
    <div class="abs submit">Submit</div>
  </section>

  <footer>
    <div class="abs footer"></div>
    <div class="abs footer-map" role="img" aria-label="Faint world map in the background"></div>
    <div class="abs f-brand">velmo.<small>finance &amp; advisory</small></div>
    <p class="abs f-p">Lorem Ipsum Dolor Amet Consectetur. Mauris Enim Dapibus Mauris Leo</p>
    <div class="abs soc" style="left:60px" aria-label="Social link"></div>
    <div class="abs soc" style="left:112px" aria-label="Social link"></div>
    <div class="abs soc" style="left:163px" aria-label="Social link"></div>
    <div class="abs soc" style="left:213px" aria-label="Social link"></div>

    <div class="abs f-h" style="left:605px">Services</div>
    <div class="abs f-l" style="left:605px">Lorem Ipsum Dolor<br>Amet Consectetur.<br>Mauris Enim<br>Dapibus Mauris</div>
    <div class="abs f-h" style="left:812px">Used Full Links</div>
    <div class="abs f-l" style="left:812px">Lorem Ipsum Dolor Amet<br>Consectetur. Mauris Enim<br>Dapibus Mauris</div>
    <div class="abs f-h" style="left:1058px">Legal</div>
    <div class="abs f-l" style="left:1058px;top:3552px">Terms Of Use<br>Privacy Policy<br>Cookie Policy</div>

    <div class="abs f-rule"></div>
    <div class="abs f-b" style="left:60px">Copyright © 2025 All Right Reserved</div>
    <div class="abs f-b" style="left:797px">Privacy Policy</div>
    <div class="abs f-b" style="left:902px">Terms Of Service</div>
    <div class="abs f-b" style="left:1023px">Cookies Settings</div>
  </footer>

</main>
</body>
</html>
```